Business cards, letter head, stationery
trial lawyer
Bright & Fun-filled
Teodoro Villaseca
Trial Lawyer
2716 kelverham, suite 300
Bellaire Texas 77538
Tevmilux@quarnela.com
Need to include:
Offices in Houston , San Antonio, and eagle pass Texas
Use winning logo

```html
<!DOCTYPE html>
<html lang="en">
<head>
<meta charset="utf-8">
<title>Teodoro Villaseca – Business Cards</title>
<link rel="stylesheet" href="https://fonts.googleapis.com/css2?family=Open+Sans:wght@400;700&display=swap">
<style>
  :root {
    --backdrop: #ece6de;
    --navy: #2b2f6b;
    --blue-deep: #1560b8;
    --blue-bright: #35a8ec;
    --green-deep: #0f6b2f;
    --green-bright: #22984a;
    --white: #ffffff;
    --ink: #1b1b1b;
    --ink-soft: #333333;
  }
  * { box-sizing: border-box; margin: 0; padding: 0; }
  html, body { width: 1200px; height: 898px; overflow: hidden; }
  body { background: var(--backdrop); position: relative; font-family: "Open Sans", Arial, sans-serif; }

  .card {
    position: absolute;
    border-radius: 26px;
    overflow: hidden;
    box-shadow: 0 6px 14px rgba(0,0,0,0.25);
  }
  .card-front { left: 336px; top: 134px; width: 516px; height: 292px; background: var(--white); }
  .card-back-green { left: 90px; top: 462px; width: 511px; height: 288px;
    background: radial-gradient(ellipse at 50% 40%, var(--green-bright), var(--green-deep)); }
  .card-back-blue { left: 640px; top: 448px; width: 509px; height: 287px;
    background: radial-gradient(ellipse at 50% 45%, var(--blue-bright), var(--blue-deep)); }

  .front-header { position: absolute; left: 0; top: 0; width: 100%; height: 140px; }

  .brand-plate {
    position: absolute;
    background: var(--white);
    display: flex;
    align-items: center;
    justify-content: center;
    gap: 10px;
  }
  .brand-square { background: var(--navy); flex: none; }
  .brand-name {
    font-family: "Open Sans", Arial, sans-serif;
    font-weight: 700;
    color: var(--navy);
    text-transform: uppercase;
    white-space: nowrap;
  }

  .card-front .brand-plate { left: 140px; top: 18px; width: 236px; height: 56px; gap: 8px; }
  .card-front .brand-square { width: 28px; height: 28px; }
  .card-front .brand-name { font-size: 14px; }

  .card-back-green .brand-plate,
  .card-back-blue .brand-plate { left: 50%; top: 50%; transform: translate(-50%, -50%); width: 314px; height: 86px; gap: 12px; }
  .card-back-green .brand-square,
  .card-back-blue .brand-square { width: 40px; height: 40px; }
  .card-back-green .brand-name,
  .card-back-blue .brand-name { font-size: 19px; }

  .front-body { position: absolute; left: 0; top: 142px; width: 100%; text-align: center; }
  .person-name { font-size: 17px; font-weight: 700; color: var(--ink); line-height: 22px; }
  .person-title { font-size: 13px; font-weight: 700; color: var(--ink); line-height: 18px; }
  .contact-list { list-style: none; margin-top: 10px; }
  .contact-list li { font-size: 8.5px; color: var(--ink-soft); line-height: 14px; }
</style>
</head>
<body>

  <section class="card card-front">
    <svg class="front-header" viewBox="0 0 516 140" preserveAspectRatio="none" aria-hidden="true">
      <defs>
        <linearGradient id="headerBlue" x1="0" y1="0" x2="1" y2="0">
          <stop offset="0" stop-color="#1a5fb4"/>
          <stop offset="0.5" stop-color="#3aa3ea"/>
          <stop offset="1" stop-color="#1a5fb4"/>
        </linearGradient>
      </defs>
      <path d="M0 0 H516 V78 C380 80 200 88 0 118 Z" fill="url(#headerBlue)"/>
      <path d="M0 118 C200 88 380 80 516 78 V86 C380 88 200 98 0 130 Z" fill="#ffffff"/>
      <path d="M0 130 C200 98 380 88 516 86 V98 C380 98 200 108 0 140 Z" fill="#137a36"/>
    </svg>

    <div class="brand-plate">
      <span class="brand-square"></span>
      <span class="brand-name">Teodoro Villaseca</span>
    </div>

    <div class="front-body">
      <h1 class="person-name">Teodoro Villaseca</h1>
      <p class="person-title">Trial Lawyer</p>
      <ul class="contact-list">
        <li>2716 kelverham, suite 300 Bellaire Texas 77538</li>
        <li>Offices in Houston, San Antonio and Eagle Pass, Texas</li>
        <li>Phone: 713-555-0148</li>
        <li>Cell: 210-555-0172</li>
        <li>Fax: 713-555-0139</li>
        <li>Email: Tevmilux@quarnela.com</li>
      </ul>
    </div>
  </section>

  <section class="card card-back-green">
    <div class="brand-plate">
      <span class="brand-square"></span>
      <span class="brand-name">Teodoro Villaseca</span>
    </div>
  </section>

  <section class="card card-back-blue">
    <div class="brand-plate">
      <span class="brand-square"></span>
      <span class="brand-name">Teodoro Villaseca</span>
    </div>
  </section>

</body>
</html>
```